Harvest Goods Federation Lobby Day 2016

I'm looking for a one page "Save the Date" flyer announcing the details of our association's annual "fly-in" or "lobby day" in Washington, DC. It will be held on Wednesday, April 13, 2016.

HGF is the nation’s largest and oldest nonprofit organization dedicated to the natural products industry. We represent around 1,500 members accounting for approximately 10,000 retail, manufacturing, wholesale, and distribution locations of natural products, including foods, dietary supplements, and health/beauty aids.

Target Market(s)

Association Membership

Font styles to use
Serif
Sans Serif

Requirements
Must have
• See last attachment "Save the Date Example." I'm looking for something simple like this.
• Also looking for something polished but not too busy. Would like the use of a Capitol Dome or other Washington, DC landmarks.

```html
<!DOCTYPE html>
<html lang="en">
<head>
<meta charset="utf-8">
<title>Harvest Goods Federation Lobby Day 2016</title>
<link rel="stylesheet" href="https://fonts.googleapis.com/css2?family=Arimo:wght@400;700&display=swap">
<style>
  :root {
    --blue: #1c7fc4;
    --blue-dark: #115f99;
    --yellow: #f6c21a;
    --green: #6cae3e;
    --ink: #1b2430;
    --white: #ffffff;
    --photo-warm: #d9c2a2;
    --photo-cool: #e8ecef;
  }
  html, body {
    margin: 0;
    padding: 0;
    width: 900px;
    height: 1200px;
    overflow: hidden;
    background: var(--white);
    font-family: "Arimo", Arial, sans-serif;
  }
  .flyer {
    position: relative;
    width: 900px;
    height: 1200px;
    background: var(--white);
    overflow: hidden;
  }
  .hero-photo {
    position: absolute;
    left: 0; top: 0;
    width: 900px; height: 560px;
    background: linear-gradient(120deg, var(--photo-cool) 0%, #cdd6dc 35%, var(--photo-warm) 70%, #b9925a 100%);
  }
  .swoosh {
    position: absolute;
    left: 0; top: 380px;
    width: 900px; height: 240px;
  }
  .brand {
    position: absolute;
    left: 60px; top: 560px;
    width: 360px;
  }
  .brand-name {
    display: flex;
    align-items: center;
    gap: 14px;
    font-weight: 700;
    font-size: 30px;
    line-height: 1.1;
    color: var(--ink);
  }
  .brand-mark {
    flex: none;
    width: 44px; height: 44px;
    background: var(--blue);
  }
  .brand-tagline {
    margin-top: 14px;
    padding-top: 10px;
    border-top: 3px solid var(--blue);
    font-style: italic;
    font-size: 19px;
    color: var(--ink);
    text-align: center;
  }
  .feature-photo {
    position: absolute;
    border-radius: 50%;
    border: 8px solid var(--white);
    box-shadow: 0 0 0 5px var(--blue);
  }
  .feature-photo.supplements {
    left: 450px; top: 520px;
    width: 230px; height: 230px;
    background: radial-gradient(circle at 40% 45%, #d8b35a, #8a8f4a 60%, #56703a);
  }
  .feature-photo.meal {
    left: 655px; top: 570px;
    width: 210px; height: 210px;
    background: radial-gradient(circle at 55% 50%, #f3e5cf, #e06b3b 55%, #6a8b3a);
  }
  .save-date {
    position: absolute;
    left: 50px; top: 730px;
    width: 370px; height: 240px;
    background: var(--blue);
    color: var(--white);
    padding: 20px 26px;
    box-sizing: border-box;
    font-weight: 700;
  }
  .save-date h1 {
    margin: 0;
    font-size: 46px;
    line-height: 1.05;
  }
  .save-date .date {
    margin: 6px 0 4px;
    font-size: 19px;
    color: var(--yellow);
  }
  .save-date .event {
    margin: 0;
    font-size: 44px;
    line-height: 1.02;
    color: var(--yellow);
  }
  .save-date .place {
    margin-top: 6px;
    font-size: 21px;
  }
  .about {
    position: absolute;
    left: 50px; top: 990px;
    width: 800px;
    margin: 0;
    font-weight: 700;
    font-size: 20px;
    line-height: 1.3;
    color: var(--ink);
  }
  .footer {
    position: absolute;
    left: 0; bottom: 0;
    width: 900px; height: 92px;
  }
  .footer-band { position: absolute; left: 0; top: 0; }
  .contact {
    position: absolute;
    top: 30px;
    height: 44px;
    display: flex;
    align-items: center;
    gap: 12px;
    color: var(--white);
    font-weight: 700;
    font-size: 30px;
    white-space: nowrap;
  }
  .contact.phone { left: 100px; }
  .contact.web { left: 480px; }
  .contact-divider {
    position: absolute;
    left: 450px; top: 33px;
    width: 3px; height: 38px;
    background: var(--white);
  }
  .icon { flex: none; width: 36px; height: 36px; }
</style>
</head>
<body>
<main class="flyer">
  <div class="hero-photo" role="img" aria-label="Photo of a young child drinking a glass of milk in a bright kitchen with fresh fruit"></div>

  <svg class="swoosh" viewBox="0 0 900 240" preserveAspectRatio="none" aria-hidden="true">
    <path d="M0 90 C250 200 600 150 900 40 L900 240 L0 240 Z" fill="#ffffff"/>
    <path d="M0 90 C250 200 600 150 900 40" fill="none" stroke="#f6c21a" stroke-width="6"/>
    <path d="M0 104 C250 214 600 164 900 54" fill="none" stroke="#1c7fc4" stroke-width="8"/>
  </svg>

  <div class="brand">
    <div class="brand-name"><span class="brand-mark"></span><span>Harvest Goods Federation</span></div>
    <div class="brand-tagline">Promoting Natural Products for Healthy Lifestyles</div>
  </div>

  <div class="feature-photo supplements" role="img" aria-label="Photo of herbs, aloe and supplement jars"></div>
  <div class="feature-photo meal" role="img" aria-label="Photo of a plated healthy meal with vegetables"></div>

  <section class="save-date">
    <h1>Save the Date</h1>
    <div class="date">Wednesday, April 13, 2016.</div>
    <p class="event">fly-in<br>lobby day</p>
    <div class="place">in Washington, DC</div>
  </section>

  <p class="about">HGF is the nation’s largest and oldest nonprofit organization dedicated to the natural products industry. We represent around 1,500 members accounting for approximately 10,000 retail, manufacturing, wholesale, and distribution locations of natural products, including foods, dietary supplements, and health/beauty aids.</p>

  <footer class="footer">
    <svg class="footer-band" width="900" height="92" viewBox="0 0 900 92" aria-hidden="true">
      <path d="M0 14 C300 0 600 0 900 14 L900 92 L0 92 Z" fill="#1c7fc4"/>
      <path d="M0 8 C300 -6 600 -6 900 8" fill="none" stroke="#f6c21a" stroke-width="5"/>
      <rect x="0" y="86" width="900" height="6" fill="#115f99"/>
    </svg>
    <div class="contact phone">
      <svg class="icon" viewBox="0 0 36 36" aria-hidden="true">
        <circle cx="18" cy="18" r="16" fill="none" stroke="#fff" stroke-width="3"/>
        <path d="M12 10 l4 0 l1 5 l-2.5 1.5 a10 10 0 0 0 5 5 l1.5 -2.5 l5 1 l0 4 a2 2 0 0 1 -2 2 a16 16 0 0 1 -14 -14 a2 2 0 0 1 2 -2z" fill="#fff"/>
      </svg>
      <span>0198-765-432</span>
    </div>
    <div class="contact-divider"></div>
    <div class="contact web">
      <svg class="icon" viewBox="0 0 36 36" aria-hidden="true">
        <path d="M8 8 L28 18 L8 28 L13 18 Z" fill="#fff"/>
      </svg>
      <span>www.harvestgoods.org</span>
    </div>
  </footer>
</main>
</body>
</html>
```